Inspire Entrepreneurs through networking, education and competitions

Background to VoK - VoK is not-for-profit organisation which inspires entrepreneurs based in Sydney, Australia. You can see a full overview of VoK in our current information TriFolds attached. We run events, training, competitions for entrepreneurs from around Australia.

I've attached our logo so that you can work with the colours. Our website is at http://sydney.vok-example.org and is currently be completely redesigned but we are not in a position to wait to get our new flyers printed since there are some large events coming up.

I'm looking for a template that we can reuse time and time again but replace the words for different topics. The final design should communicate:
Inspiration to entrepreneurs
Inclusive (age, gender, race, etc.)
Growth and acceleration

Industry/Entity Type

Education

Requirements
Must have
• Work with the colour scheme of the current logo

```html
<!DOCTYPE html>
<html lang="en">
<head>
<meta charset="utf-8">
<title>VoK Growth Round Tables Trifold</title>
<link href="https://fonts.googleapis.com/css2?family=Open+Sans:wght@400;600;700;800&family=Roboto+Slab:wght@600;700&display=swap" rel="stylesheet">
<style>
:root{
  --navy:#0a2f7a;
  --blue:#1454b8;
  --bright:#1f6fd6;
  --cyan:#4fb3f0;
  --sky:#d9ecfb;
  --red:#d3272f;
  --ink:#24324a;
  --muted:#6b7688;
  --white:#ffffff;
  --page:#f4f5f7;
}
*{box-sizing:border-box;margin:0;padding:0}
html,body{width:750px;height:1200px;overflow:hidden;background:var(--page)}
body{font-family:"Open Sans",Arial,sans-serif;color:var(--white);position:relative}
.sheet{position:absolute;left:25px;width:700px;height:490px;display:flex;box-shadow:0 6px 18px rgba(0,0,0,.25)}
.sheet.outside{top:60px}
.sheet.inside{top:650px}
.panel{position:relative;width:233.33px;height:100%;overflow:hidden}
.panel + .panel{border-left:1px solid rgba(255,255,255,.15)}
.deep{background:linear-gradient(160deg,var(--navy) 0%,var(--blue) 55%,var(--navy) 100%)}
.mid{background:linear-gradient(170deg,var(--blue) 0%,var(--bright) 60%,var(--blue) 100%)}
.light{background:var(--white);color:var(--ink)}
.pad{padding:20px 18px}
h2,h3,.cover-title,.events-head{font-family:"Roboto Slab",Georgia,serif}
h2{font-size:14px;font-weight:700;color:var(--cyan);margin-bottom:8px;line-height:1.2}
h3{font-size:11.5px;font-weight:700;color:var(--cyan);margin:10px 0 4px}
p{font-size:7.6px;line-height:1.5;margin-bottom:7px}
.quote{font-style:italic;color:var(--sky)}
.author{font-size:7px;font-weight:700;text-align:right;margin-top:-4px;margin-bottom:9px;color:var(--white)}
.footer-url{position:absolute;bottom:10px;left:0;right:0;text-align:center;font-size:8px;font-weight:600;letter-spacing:.5px;color:var(--white)}
.ticks{list-style:none;margin:4px 0 10px}
.ticks li{font-size:7.6px;line-height:1.45;padding-left:12px;position:relative;margin-bottom:4px}
.ticks li::before{content:"";position:absolute;left:0;top:3px;width:6px;height:6px;border-radius:50%;background:var(--cyan)}
.contact{display:flex;align-items:center;gap:7px;font-size:7.6px;margin-bottom:6px}
.contact svg{width:14px;height:14px;flex:none}
.support-label{font-size:7px;font-weight:600;color:var(--sky);margin:12px 0 5px}
.badge{height:30px;background:var(--white);margin-bottom:6px;border-radius:2px;position:relative}
.badge::after{content:"";position:absolute;left:10px;top:8px;width:14px;height:14px;background:var(--blue)}
.badge.gov::after{background:var(--navy);border-radius:50%}
.brand{display:flex;align-items:center;justify-content:center;gap:7px;margin-top:32px}
.brand-square{width:12px;height:12px;background:var(--navy)}
.brand-name{font-family:"Open Sans",Arial,sans-serif;font-size:18px;font-weight:700;color:var(--navy);line-height:1;letter-spacing:.5px}
.cover-title{text-align:center;margin-top:20px}
.cover-title .t1{font-size:13px;font-weight:700;color:var(--red)}
.cover-title .t2{font-size:11px;font-weight:600;color:var(--blue);margin-top:3px}
.cover-photo{position:absolute;left:38px;top:160px;width:158px;height:158px;border-radius:50%;border:5px solid var(--white);box-shadow:0 0 0 3px var(--bright);background:radial-gradient(circle at 55% 45%,#7fc3f5 0%,#2a6fcb 45%,#0b2a66 100%)}
.wave{position:absolute;left:0;width:100%}
.photo{position:absolute;left:0;width:100%}
.photo.coins{top:150px;height:165px;background:linear-gradient(135deg,#7f9c3a 0%,#c7a955 45%,#5c4a2b 100%)}
.photo.bulb{top:315px;height:175px;background:radial-gradient(circle at 45% 40%,#bfe4ff 0%,#3d7fd1 40%,#0b2d6c 100%)}
.events-head{background:var(--blue);color:var(--white);font-size:13px;font-weight:700;padding:14px 16px 10px}
.event{display:flex;gap:9px;padding:9px 14px;border-bottom:1px solid #e2e7ef}
.date{flex:none;width:32px;height:36px;background:var(--blue);color:var(--white);text-align:center;border-radius:2px}
.date .m{display:block;font-size:6.5px;font-weight:700;background:var(--navy);padding:2px 0}
.date .d{display:block;font-size:14px;font-weight:800;line-height:22px}
.event-text .name{font-size:8px;font-weight:700;color:var(--blue);line-height:1.3}
.event-text .info{font-size:7px;color:var(--muted);line-height:1.4}
.notice{background:var(--white);color:var(--blue);padding:8px 10px;margin-top:8px;border-radius:2px;text-align:center;font-size:7.6px;font-weight:600;line-height:1.45}
.photo.books{bottom:0;height:105px;background:linear-gradient(160deg,#6c4a2a 0%,#c49a62 50%,#3a2616 100%)}
</style>
</head>
<body>

<section class="sheet outside">
  <div class="panel deep">
    <div class="pad">
      <h2>A brief introduction to VoK</h2>
      <p>VoK Sydney is a not-for-profit network that inspires founders through mentoring, education, funding access and events across Australia.</p>
      <p>Our members include successful entrepreneurs, corporate leaders and investors who share experience freely with the next generation of business builders.</p>
      <p class="quote">“VoK helped me meet the right people at the right time and grow my company faster than I imagined.”</p>
      <p class="author">Henry Walsh, Founder, Brightlane Labs</p>
      <p class="quote">“The round tables gave our team honest feedback and practical ideas we applied the very next week.”</p>
      <p class="author">Jill Mercer, Director, Coastal Ventures</p>
      <p>Join a community that celebrates every founder, regardless of age, gender or background.</p>
    </div>
    <div class="footer-url">sydney.vok-example.org</div>
  </div>

  <div class="panel mid">
    <div class="pad">
      <p>VoK Growth Round Tables bring small groups of founders together with an experienced chair to solve real challenges.</p>
      <p>Each session runs monthly and focuses on scaling, funding, hiring and leadership.</p>
      <h3>So what makes us different?</h3>
      <ul class="ticks">
        <li>Peers who understand the pressure of growth</li>
        <li>Chairs who have built and sold companies</li>
        <li>A safe, confidential and inclusive setting</li>
        <li>Direct links to investors and partners</li>
      </ul>
      <div class="contact">
        <svg viewBox="0 0 14 14"><circle cx="7" cy="7" r="7" fill="#fff"/><circle cx="7" cy="7" r="4.2" fill="none" stroke="#1454b8" stroke-width="1"/><path d="M2.8 7h8.4M7 2.8c-2 2.5-2 5.9 0 8.4M7 2.8c2 2.5 2 5.9 0 8.4" fill="none" stroke="#1454b8" stroke-width=".8"/></svg>
        www.vok-example.org
      </div>
      <div class="contact">
        <svg viewBox="0 0 14 14"><circle cx="7" cy="7" r="7" fill="#fff"/><path d="M4.5 3.6l1.5-.3.8 1.9-1 .8a5 5 0 0 0 2.2 2.2l.8-1 1.9.8-.3 1.5c-3.4.3-6.2-2.5-5.9-5.9z" fill="#1454b8"/></svg>
        +61 2 5550 1234
      </div>
      <div class="contact">
        <svg viewBox="0 0 14 14"><circle cx="7" cy="7" r="7" fill="#fff"/><rect x="3.5" y="4.5" width="7" height="5" fill="none" stroke="#1454b8" stroke-width=".9"/><path d="M3.5 4.5L7 7.4l3.5-2.9" fill="none" stroke="#1454b8" stroke-width=".9"/></svg>
        info@vok-example.org
      </div>
      <div class="support-label">Supported by</div>
      <div class="badge"></div>
      <div class="badge gov"></div>
    </div>
    <div class="footer-url">sydney.vok-example.org</div>
  </div>

  <div class="panel light">
    <div class="brand"><span class="brand-square"></span><span class="brand-name">VoK Sydney</span></div>
    <div class="cover-title">
      <div class="t1">Growth Round Tables</div>
      <div class="t2">Launching February 2016</div>
    </div>
    <svg class="wave" style="bottom:0;height:190px" viewBox="0 0 233 190" preserveAspectRatio="none">
      <path d="M0 70 C60 40 150 40 233 10 V190 H0Z" fill="#1f6fd6"/>
      <path d="M0 95 C70 65 160 70 233 40 V190 H0Z" fill="#0a2f7a"/>
    </svg>
    <div class="cover-photo" role="img" aria-label="Photo of a hand touching a glowing digital network"></div>
    <div class="footer-url">sydney.vok-example.org</div>
  </div>
</section>

<section class="sheet inside">
  <div class="panel deep">
    <div class="pad">
      <h2>About VoK</h2>
      <p>VoK Sydney is part of a global network that supports entrepreneurs at every stage, from first idea to international expansion. We run events, training programs and competitions across Australia.</p>
    </div>
    <div class="photo coins" role="img" aria-label="Photo of seedlings growing from stacks of coins"></div>
    <div class="photo bulb" role="img" aria-label="Photo of a glowing light bulb"></div>
    <svg class="wave" style="top:300px;height:30px" viewBox="0 0 233 30" preserveAspectRatio="none">
      <path d="M0 18 C80 2 150 30 233 8 V22 C150 30 80 10 0 26Z" fill="#4fb3f0"/>
    </svg>
  </div>

  <div class="panel light">
    <div class="events-head">Upcoming Events</div>
    <div class="event"><div class="date"><span class="m">FEB</span><span class="d">09</span></div><div class="event-text"><div class="name">Growth Round Table Launch</div><div class="info">Sydney CBD, 6:00pm to 8:30pm</div></div></div>
    <div class="event"><div class="date"><span class="m">FEB</span><span class="d">23</span></div><div class="event-text"><div class="name">Founder Breakfast Series</div><div class="info">Barangaroo, 7:30am to 9:00am</div></div></div>
    <div class="event"><div class="date"><span class="m">MAR</span><span class="d">08</span></div><div class="event-text"><div class="name">Women in Business Forum</div><div class="info">Parramatta, 5:30pm to 8:00pm</div></div></div>
    <div class="event"><div class="date"><span class="m">MAR</span><span class="d">22</span></div><div class="event-text"><div class="name">Pitch Night Competition</div><div class="info">Surry Hills, 6:00pm to 9:00pm</div></div></div>
    <div class="event"><div class="date"><span class="m">APR</span><span class="d">12</span></div><div class="event-text"><div class="name">Investor Readiness Workshop</div><div class="info">North Sydney, 9:00am to 1:00pm</div></div></div>
    <div class="event"><div class="date"><span class="m">APR</span><span class="d">26</span></div><div class="event-text"><div class="name">Scale-Up Masterclass</div><div class="info">Sydney CBD, 2:00pm to 5:00pm</div></div></div>
  </div>

  <div class="panel mid">
    <div class="pad">
      <h3 style="margin-top:0">When does it run?</h3>
      <p>Round tables meet on the second Tuesday of every month from February to November.</p>
      <h3>What is my commitment?</h3>
      <p>Members attend ten sessions a year and share one business challenge at each meeting.</p>
      <h3>How do I apply?</h3>
      <p>Submit a short application online. Eligible founders:</p>
      <ul class="ticks">
        <li>Revenue above $500k</li>
        <li>Operating for two years or more</li>
        <li>Committed to growth</li>
      </ul>
      <div class="notice">Applications close 31 January 2016. Places are limited to twelve founders per table.</div>
    </div>
    <div class="photo books" role="img" aria-label="Photo of open books on a desk"></div>
  </div>
</section>

</body>
</html>
```